Educational non-profit needs an End of the Year Flyer

We need a flyer to mail to our supporters asking for donations to our program. Hillcrest Open Learning Hub runs after school programs for low-income students in Pasadena, CA. This is our end of the year mailing to supporters asking them to finish out the year with their contributions so that we can meet our budget.

Target Market(s)

Donors and supporters of organization

Industry/Entity Type

Non-Profit

Font styles to use
Serif

Colors

Designer to choose colors to be used in the design.

Requirements
Must have
• The project should fit on a 6x9" card, and be printed on front and back. It should show pictures, use the copy I have included, a space for a label address, a stamp, and the return address.
Nice to have
• eye-catching, fun

```html
<!DOCTYPE html>
<html lang="en">
<head>
<meta charset="utf-8">
<title>Hillcrest Open Learning Hub – Year-End Mailer</title>
<link href="https://fonts.googleapis.com/css2?family=PT+Sans:wght@400;700&family=Oswald:wght@400;500&display=swap" rel="stylesheet">
<style>
  :root{
    --bg:#e9e6e1;
    --paper:#ffffff;
    --charcoal:#3d3d3d;
    --ink:#222222;
    --sky:#1fa0d8;
    --royal:#1d4fb8;
    --sun:#fff200;
    --rule:#9a9a9a;
  }
  *{box-sizing:border-box;margin:0;padding:0}
  html,body{width:1200px;height:1200px;overflow:hidden;background:var(--bg);font-family:"PT Sans",sans-serif;color:var(--ink)}
  .card{position:absolute;background:var(--paper);box-shadow:0 4px 14px rgba(0,0,0,.18)}
  .front{left:228px;top:45px;width:744px;height:497px}
  .back{left:230px;top:610px;width:741px;height:494px}
  .abs{position:absolute}
  .photo{position:absolute;border:1.5px solid #333}
  .photo-choir{left:22px;top:20px;width:703px;height:241px;background:linear-gradient(180deg,#2a2520 0%,#5b3a38 45%,#8a3c3c 70%,#2e2a2a 100%)}
  .photo-hoops{left:22px;top:270px;width:207px;height:149px;background:linear-gradient(160deg,#d9cfc4,#8a5a52 60%,#3a2e33)}
  .photo-guitar{left:517px;top:270px;width:208px;height:149px;background:linear-gradient(180deg,#c9b4a0 0%,#a88a70 60%,#e8e4de 75%,#f3f1ee)}
  .photo-flex{left:22px;top:98px;width:360px;height:121px;border-color:#ddd;background:linear-gradient(180deg,#b65a3e 0%,#9c4b34 50%,#2f4b5e 80%,#1e2a3a)}
  .logo-box{left:22px;top:20px;width:82px;height:100px;background:var(--paper);display:flex;align-items:center;justify-content:center;text-align:center;padding:6px;font-size:11px;font-weight:700;line-height:1.2;color:var(--ink)}
  .appeal{left:234px;top:270px;width:278px;height:149px;background:var(--sun);padding:6px}
  .appeal-inner{width:100%;height:100%;border:1px solid #b9a800;display:flex;flex-direction:column;align-items:center;justify-content:center;font-family:"Oswald",sans-serif;color:var(--royal);text-align:center}
  .appeal-lead{font-size:22px;line-height:1.1;letter-spacing:-.3px}
  .appeal-year{font-size:46px;line-height:1.1;font-weight:500;letter-spacing:-.5px}
  .contact-band{left:0;top:435px;width:744px;height:62px;background:var(--charcoal);display:flex;color:#fff}
  .contact-band div{display:flex;align-items:center;justify-content:center;border-right:1px solid #8a8a8a}
  .contact-band div:last-child{border-right:0}
  .cb-phone{width:212px;font-size:20px}
  .cb-mail{width:280px;font-size:15px;letter-spacing:1.6px}
  .cb-web{width:252px;font-size:15px;letter-spacing:1.6px}
  .cb-icon{display:inline-block;width:9px;height:9px;margin-right:5px}
  .story{left:0;top:0;width:385px;height:396px;background:var(--charcoal);color:#fff}
  .story-text{left:22px;top:27px;width:354px;font-size:10.6px;line-height:1.32;text-align:justify}
  .budget-label{left:22px;top:224px;font-size:14px;font-weight:700}
  .amount{top:244px;width:143px;height:37px;background:var(--sky);border:1.5px dashed #fff;font-family:"Oswald",sans-serif;font-size:32px;line-height:34px;text-align:center;color:#fff;letter-spacing:-.5px}
  .amount sup{font-size:9px;vertical-align:top;line-height:14px}
  .amount-total{left:24px}
  .amount-donors{left:190px}
  .donor-note{left:186px;top:286px;font-size:11.5px}
  .ask{left:24px;top:305px;width:346px;height:31px;background:#fff;font-family:"Oswald",sans-serif;font-size:17px;line-height:31px;text-align:center;color:var(--royal);letter-spacing:-.2px}
  .greeting{left:22px;top:340px;font-size:20.5px}
  .footnote{left:26px;top:372px;font-size:9.5px;font-weight:700;display:flex;align-items:center;gap:8px}
  .footnote span.pay{background:#fff;color:var(--royal);padding:1px 5px;font-weight:700}
  .info-band{left:0;top:409px;width:385px;height:67px;background:var(--sky);color:#fff;font-size:9.6px;line-height:1.3;display:flex}
  .info-col{padding:7px 0 0 27px}
  .info-col p{margin-bottom:6px}
  .info-col .addr{margin-bottom:0}
  .info-left{width:197px;border-right:1px solid #d7eef8;padding-left:27px}
  .info-right{padding-left:17px}
  .stamp{left:651px;top:44px;width:53px;height:55px;border:1px solid var(--rule)}
  .addr-line{left:522px;width:183px;height:1px;background:var(--rule)}
  .return-name{left:610px;top:372px;width:130px;text-align:center;font-size:12px;font-weight:700;line-height:1.25}
</style>
</head>
<body>

<section class="card front">
  <div class="photo photo-choir" role="img" aria-label="Large group of children in festive clothes on a stage with string lights for a holiday concert"></div>
  <div class="abs logo-box">Hillcrest Open Learning Hub</div>
  <div class="photo photo-hoops" role="img" aria-label="Group of smiling girls holding basketballs in a gym"></div>
  <div class="abs appeal">
    <div class="appeal-inner">
      <div class="appeal-lead">We need your help to finish out</div>
      <div class="appeal-year">2018 strong!</div>
    </div>
  </div>
  <div class="photo photo-guitar" role="img" aria-label="Students playing acoustic guitars on a school stage"></div>
  <div class="abs contact-band">
    <div class="cb-phone">
      <svg class="cb-icon" viewBox="0 0 10 10"><path d="M2 1l2 2-1 1.2c.6 1.2 1.6 2.2 2.8 2.8L7 6l2 2-1.3 1.3C4.5 9 1 5.5.7 2.3z" fill="#fff"/></svg>(626) 555-0142
    </div>
    <div class="cb-mail">
      <svg class="cb-icon" viewBox="0 0 10 10"><rect x="0.5" y="2" width="9" height="6" fill="#fff"/><path d="M.5 2l4.5 3.5L9.5 2" stroke="#3d3d3d" fill="none"/></svg>hello@brightpathkids.org
    </div>
    <div class="cb-web">
      <svg class="cb-icon" viewBox="0 0 10 10"><circle cx="5" cy="5" r="4" fill="none" stroke="#fff" stroke-width="1.4"/><path d="M1 5h8" stroke="#fff"/></svg>www.brightpathkids.org
    </div>
  </div>
</section>

<section class="card back">
  <div class="abs story">
    <p class="abs story-text">We have had a wonderful 25th year of serving the children and families of Pasadena here at Hillcrest Open Learning Hub with high quality afterschool programs. Hundreds and hundreds of students have been a part of the Bright Path Kids Club family.</p>
    <div class="photo photo-flex" role="img" aria-label="Group of young students flexing their arms in front of a brick wall"></div>
    <p class="abs budget-label">Our annual budget is:</p>
    <div class="abs amount amount-total">$275,000<sup>*</sup></div>
    <div class="abs amount amount-donors">$100,000<sup>*</sup></div>
    <p class="abs donor-note">we count on from individual donors.</p>
    <div class="abs ask">Will you join with us for an end of the year contribution?</div>
    <p class="abs greeting">Merry Christmas from all of us at HOLH!</p>
    <p class="abs footnote">* You can give online through QuickGive <span class="pay">QuickGive</span></p>
  </div>
  <div class="abs info-band">
    <div class="info-col info-left">
      <p>☏ (626) 555-0142</p>
      <p class="addr">⌖ Hillcrest Open Learning Hub<br>&nbsp;&nbsp;&nbsp;214 N. Alder Ave.<br>&nbsp;&nbsp;&nbsp;Pasadena, CA 91100</p>
    </div>
    <div class="info-col info-right">
      <p>◍ www.brightpathkids.org</p>
      <p>✉ hello@brightpathkids.org</p>
      <p>▪ Hillcrest Open Learning Hub</p>
    </div>
  </div>
  <div class="abs stamp"></div>
  <div class="abs addr-line" style="top:162px"></div>
  <div class="abs addr-line" style="top:204px"></div>
  <div class="abs addr-line" style="top:244px"></div>
  <div class="abs addr-line" style="top:284px"></div>
  <div class="abs return-name">Hillcrest Open<br>Learning Hub</div>
</section>

</body>
</html>
```